Collagen Tub Packaging Design for a New Brand

PLEASE DON'T SEND ANY NEW DESIGNS WE JUST HAVE TO DECIDE WITH MY PARTNERS THANKS A LOT.
I've created a very detailed document & design examples of what we like in certain designs and what we don't.

There are 3 documents:
1- Brief for the Design (please read it before designing)
2- Brand Design Examples that we like (and why we like them)
3- Die cut for the packaging design. This will be it's dimensions.

We are NOT looking for someone to micro-manage. In contrast, we want someone to help us express our ideas better with their design. Nothing I say in these briefs are there to limit the creativity of the designer, because if we knew exactly what we wanted we would do it ourselves but we trust the designer's expertise in this packaging design.

In short: We want our brand to feel premium, high-quality & trust worthy with it's design not feeling very busy or bloated. We don't have a logo source file, but you'll get the idea of what we want when you see it).

Let me know if you have any further questions, will answer each question real fast.

Thanks.

Target Market(s)

Pretty much everyone above 25+ in Turkey because nearly all of them are using are collagens so our audience is wild.

Industry/Entity Type

Collagen - Health, Wellness & Supplements

Font styles to use
Serif
Sans Serif

Colors

Designer to choose colors to be used in the design.

Requirements
Must have
• Our design should be distinct, a design style which everyone can identify from 10 meters away if they know the product. This is a MUST have for us. It's up to designer to achieve it. This can be just a simple color palette aswell.
Should not have
• It shouldn't feel bloated and very busy. Please avoid very detailed icons (as a rule of thumb, if you can make it work great)

```html
<!DOCTYPE html>
<html lang="en">
<head>
<meta charset="utf-8">
<title>Colvera Hydrolyzed Collagen Peptides – Packaging</title>
<link href="https://fonts.googleapis.com/css2?family=Montserrat:wght@300;400;500;700;800&family=Oswald:wght@400;500&display=swap" rel="stylesheet">
<style>
  :root {
    --royal: #1f45c9;
    --royal-light: #4a7fd8;
    --navy: #0a1b96;
    --deep: #061385;
    --silver: #c8cbd1;
    --silver-light: #eef0f3;
    --silver-dark: #a9adb4;
    --paper: #ececec;
    --ink: #1a1a1a;
    --white: #ffffff;
    --grey-text: #6f6f72;
  }
  html, body {
    margin: 0;
    padding: 0;
    width: 1187px;
    height: 1200px;
    overflow: hidden;
    background: var(--paper);
    font-family: "Montserrat", sans-serif;
  }
  .canvas { position: relative; width: 1187px; height: 1200px; }
  .canvas svg { position: absolute; inset: 0; }
  .brand-word { font-family: "Montserrat", sans-serif; font-weight: 800; fill: var(--silver); letter-spacing: -2px; }
  .brand-word--banner { fill: var(--silver-light); }
  .product-line { font-family: "Montserrat", sans-serif; font-weight: 500; fill: var(--silver); letter-spacing: 1px; }
  .product-line--bold { font-weight: 800; }
  .spaced-title { font-family: "Montserrat", sans-serif; font-weight: 300; fill: var(--grey-text); font-size: 13px; letter-spacing: 15px; }
  .pill-text { font-family: "Montserrat", sans-serif; font-weight: 700; fill: var(--royal); font-size: 9.5px; }
  .extra-text { font-family: "Montserrat", sans-serif; font-weight: 400; fill: var(--silver-light); font-size: 10.5px; }
  .extra-text--bold { font-weight: 700; }
  .stat-value { font-family: "Oswald", sans-serif; font-weight: 500; fill: var(--silver-light); font-size: 18px; }
  .stat-unit { font-size: 11px; }
  .stat-label { font-family: "Oswald", sans-serif; font-weight: 400; fill: var(--silver-light); font-size: 5.5px; }
  .band-text { font-family: "Montserrat", sans-serif; font-weight: 400; fill: var(--ink); font-size: 12px; }
  .band-text--strong { font-family: "Oswald", sans-serif; font-weight: 500; font-size: 16px; }
  .band-text--bold { font-weight: 800; font-size: 12.5px; }
</style>
</head>
<body>
<main class="canvas">
<svg width="1187" height="1200" viewBox="0 0 1187 1200" xmlns="http://www.w3.org/2000/svg">
  <defs>
    <linearGradient id="banner-grad" x1="0" y1="0" x2="1" y2="0">
      <stop offset="0" stop-color="#2a5ad6"/>
      <stop offset="0.35" stop-color="#0d1f9e"/>
      <stop offset="0.55" stop-color="#0f28a6"/>
      <stop offset="0.78" stop-color="#4a7fd8"/>
      <stop offset="1" stop-color="#0a1d9e"/>
    </linearGradient>
    <linearGradient id="label-grad" x1="0" y1="0" x2="1" y2="0">
      <stop offset="0" stop-color="#1e44c8"/>
      <stop offset="0.45" stop-color="#2a55cf"/>
      <stop offset="0.65" stop-color="#4a7fd8"/>
      <stop offset="1" stop-color="#1538b8"/>
    </linearGradient>
    <linearGradient id="silver-grad" x1="0" y1="0" x2="1" y2="0">
      <stop offset="0" stop-color="#a9adb4"/>
      <stop offset="0.5" stop-color="#eef0f3"/>
      <stop offset="1" stop-color="#b8bcc2"/>
    </linearGradient>
    <radialGradient id="molecule-grad" cx="0.45" cy="0.45" r="0.55">
      <stop offset="0" stop-color="#6f96e6"/>
      <stop offset="1" stop-color="#2a5ad6" stop-opacity="0"/>
    </radialGradient>
  </defs>

  <g class="header-banner">
    <rect x="0" y="0" width="1187" height="241" fill="url(#banner-grad)"/>
    <circle cx="170" cy="160" r="240" fill="url(#molecule-grad)" role="img" aria-label="Abstract molecular network illustration"/>
    <text class="brand-word brand-word--banner" x="602" y="142" font-size="64" text-anchor="middle">Colvera</text>
  </g>

  <text class="spaced-title" x="593" y="284" text-anchor="middle">HYDROLYZED COLLAGEN PEPTIDES</text>

  <g class="tub-label">
    <rect x="220" y="600" width="401" height="302" fill="url(#label-grad)"/>
    <rect x="220" y="902" width="401" height="50" fill="url(#silver-grad)"/>

    <g class="label-cross" fill="#1f46c4" opacity="0.85">
      <path d="M537 672 L577 672 L573 710 L615 710 L605 750 L565 750 L561 790 L521 790 L525 750 L497 750 L507 710 L533 710 Z"/>
    </g>

    <text class="brand-word" x="262" y="684" font-size="64">Colvera</text>

    <text class="product-line" x="267" y="754" font-size="24">HYDROLYZED</text>
    <text class="product-line product-line--bold" x="267" y="782" font-size="24">COLLAGEN</text>
    <text class="product-line" x="267" y="810" font-size="24">PEPTIDES</text>

    <rect x="259" y="827" width="155" height="25" rx="12.5" fill="var(--silver)"/>
    <text class="pill-text" x="336" y="838" text-anchor="middle">HIGH ABSORPTION</text>
    <text class="pill-text" x="336" y="848" text-anchor="middle">HIGH-QUALITY MATERIAL</text>

    <path d="M477 759 L487 759 L486 768 L496 768 L494 777 L484 777 L483 786 L473 786 L474 777 L465 777 L467 768 L475 768 Z" fill="var(--white)"/>
    <path d="M475 786 C458 805 450 835 449 860" fill="none" stroke="var(--silver-light)" stroke-width="1"/>
    <circle cx="476" cy="785" r="2" fill="var(--white)"/>
    <circle cx="449" cy="860" r="2" fill="var(--white)"/>

    <text class="extra-text" x="478" y="811"><tspan class="extra-text--bold">SI+</tspan>  (SILISIUM PLUS)</text>
    <text class="extra-text" x="478" y="826"><tspan class="extra-text--bold">C+</tspan>   (VITAMIN C PLUS)</text>

    <g class="nutrition-stats">
      <text class="stat-value" x="476" y="855">12<tspan class="stat-unit">G</tspan></text>
      <text class="stat-label" x="477" y="864">COLLAGEN</text>
      <line x1="502" y1="838" x2="502" y2="866" stroke="var(--silver-light)" stroke-width="0.8"/>
      <text class="stat-value" x="506" y="855">11<tspan class="stat-unit">G</tspan></text>
      <text class="stat-label" x="507" y="864">PROTEIN</text>
      <line x1="532" y1="838" x2="532" y2="866" stroke="var(--silver-light)" stroke-width="0.8"/>
      <text class="stat-value" x="536" y="855">0<tspan class="stat-unit">G</tspan></text>
      <text class="stat-label" x="537" y="864">SUGAR</text>
      <line x1="556" y1="838" x2="556" y2="866" stroke="var(--silver-light)" stroke-width="0.8"/>
      <text class="stat-value" x="560" y="855">0<tspan class="stat-unit">G</tspan></text>
      <text class="stat-label" x="561" y="864">CARBS</text>
      <line x1="581" y1="838" x2="581" y2="866" stroke="var(--silver-light)" stroke-width="0.8"/>
      <text class="stat-value" x="585" y="855">0<tspan class="stat-unit">G</tspan></text>
      <text class="stat-label" x="586" y="864">FAT</text>
    </g>

    <text class="band-text" x="263" y="927"><tspan class="band-text--strong">620G</tspan> OF COLLAGEN POWDER</text>
    <text class="band-text band-text--bold" x="479" y="927">FLAVOURLESS</text>
  </g>

  <g class="lid-top">
    <circle cx="848" cy="756" r="206" fill="var(--royal)"/>
    <circle cx="848" cy="756" r="180" fill="var(--navy)"/>
    <circle cx="848" cy="756" r="153" fill="none" stroke="var(--silver)" stroke-width="1.2"/>
    <path d="M925 789 L957 789 L954 821 L988 821 L980 853 L947 853 L944 893 L912 893 L915 853 L891 853 L899 821 L921 821 Z" fill="var(--deep)"/>
    <text class="brand-word" x="735" y="734" font-size="60">Colvera</text>
    <text class="product-line" x="745" y="787" font-size="23">HYDROLYZED</text>
    <text class="product-line product-line--bold" x="745" y="813" font-size="23">COLLAGEN</text>
    <text class="product-line" x="745" y="839" font-size="23">PEPTIDES</text>
  </g>
</svg>
</main>
</body>
</html>
```